Webdesign für Institut für Morgenlicht & Weitblick
Zielgruppe
Bright Path Institute - Heiter und Zielstrebig wohnen
Wir sind eine neu gegründete Academy wo es um die Erreichung von Glück, Erfolg, Zufriedenheit, Motivation, Lernen geht. Wir bieten Seminare, Vorträge, Hypnosetherapie, Mentaltraining, Feuerlauf an.
Aufgabenstellung
unten angehangen ein Bild von mir, dazu Bilder zu den verschiedenen Angeboten und die Geschäftspapiere, die der Seite mit als Grundlage dienen sollten.

```html
<!DOCTYPE html>
<html lang="de">
<head>
<meta charset="utf-8">
<title>Bright Path Institute – Hypnose</title>
<link rel="stylesheet" href="https://fonts.googleapis.com/css2?family=Open+Sans:wght@400;600;700&family=Arimo:wght@700&display=swap">
<style>
  :root {
    --navy: #2b3f8f;
    --blue-mid: #3a6fbf;
    --blue-light: #4a9ad8;
    --sky: #e2eff8;
    --accent: #3a93d6;
    --tab-light: #8fcdf5;
    --tab-dark: #3a93d6;
    --text: #23306a;
    --quote: #4b7bb5;
    --white: #ffffff;
    --photo: #c9b3a4;
  }
  * { box-sizing: border-box; margin: 0; padding: 0; }
  html, body { width: 768px; height: 1200px; overflow: hidden; }
  body { position: relative; background: var(--sky); font-family: "Open Sans", sans-serif; color: var(--text); }

  .hero-bg { position: absolute; left: 0; top: 0; width: 768px; height: 340px; }

  .brand { position: absolute; left: 66px; top: 26px; display: flex; align-items: center; gap: 8px; }
  .brand-dot { width: 38px; height: 38px; border-radius: 50%; border: 3px solid var(--blue-light); }
  .brand-name { color: var(--white); font-weight: 600; font-size: 15px; line-height: 1.15; }
  .brand-name small { display: block; font-size: 8.5px; font-weight: 600; color: var(--white); }

  .main-nav { position: absolute; top: 39px; left: 455px; display: flex; gap: 0; }
  .main-nav a { color: var(--white); text-decoration: none; font-size: 7.5px; font-weight: 600; letter-spacing: 1px; line-height: 17px; }
  .main-nav .nav-hypnose { background: var(--white); color: var(--navy); font-weight: 700; padding: 0 4px; }
  .main-nav .nav-about { margin-left: 37px; }
  .main-nav .nav-courses { margin-left: 41px; }

  .hero-title { position: absolute; left: 51px; top: 146px; color: var(--white); font-weight: 700; }
  .hero-title .line1 { display: block; font-size: 38px; line-height: 44px; }
  .hero-title .line2 { display: block; font-size: 23.5px; line-height: 30px; }
  .hero-intro { position: absolute; left: 51px; top: 227px; width: 370px; color: var(--white); font-size: 10px; line-height: 16px; font-weight: 600; }

  .side-tabs { position: absolute; left: 621px; top: 304px; width: 103px; }
  .side-tabs a { display: block; height: 24.5px; line-height: 24.5px; text-align: center; color: var(--white); text-decoration: none; font-size: 9.5px; font-weight: 700; letter-spacing: 0.6px; }
  .side-tabs .tab-active { background: var(--tab-light); }
  .side-tabs .tab { background: var(--tab-dark); }

  .article-head { position: absolute; left: 0; width: 768px; top: 313px; text-align: center; }
  .article-head h1 { font-size: 23px; font-weight: 700; color: var(--quote); line-height: 32px; }
  .article-head h2 { font-size: 14.5px; font-weight: 700; color: var(--accent); line-height: 20px; }

  .quote-mark { position: absolute; font-family: Georgia, serif; font-weight: 700; color: var(--quote); font-size: 52px; line-height: 1; }
  .quote-open { left: 155px; top: 350px; }
  .quote-close { left: 578px; top: 912px; }

  .article-body { position: absolute; left: 187px; top: 383px; width: 395px; font-size: 8.3px; line-height: 12px; }
  .article-body p { margin-bottom: 10.6px; }
  .article-body h3 { font-size: 10px; color: var(--accent); font-weight: 700; margin: 12px 0 9px; }

  .footer { position: absolute; left: 0; top: 981px; width: 768px; height: 219px; background: var(--white); }
  .footer-art { position: absolute; left: 0; top: 0; width: 768px; height: 170px; }
  .portrait { position: absolute; left: 237px; top: 33px; width: 106px; height: 106px; border-radius: 50%; border: 1.5px solid var(--accent); background: radial-gradient(circle at 50% 45%, #d9c4b6 0 40%, #9fb4cf 41% 100%); }
  .footer-divider { position: absolute; left: 372px; top: 69px; width: 1.5px; height: 33px; background: var(--accent); }
  .contact { position: absolute; left: 396px; top: 52px; font-family: "Arimo", sans-serif; font-weight: 700; color: var(--quote); }
  .contact .name { font-size: 15px; line-height: 17px; color: var(--accent); }
  .contact .address { font-size: 11.5px; line-height: 14px; }
  .contact .phones { margin-top: 13px; font-size: 10px; line-height: 12px; }
  .contact .phones .or { color: var(--navy); }
</style>
</head>
<body>
  <svg class="hero-bg" viewBox="0 0 768 340" aria-hidden="true">
    <defs>
      <linearGradient id="heroGrad" x1="0" y1="0" x2="1" y2="1">
        <stop offset="0" stop-color="#2a3c8c"/>
        <stop offset="0.55" stop-color="#3360b0"/>
        <stop offset="1" stop-color="#3f8fd2"/>
      </linearGradient>
    </defs>
    <polygon points="0,0 768,0 768,263 0,340" fill="url(#heroGrad)"/>
  </svg>

  <header>
    <div class="brand">
      <span class="brand-dot"></span>
      <span class="brand-name">Bright Path Institute<small>Heiter und Zielstrebig wohnen.</small></span>
    </div>
    <nav class="main-nav">
      <a class="nav-hypnose" href="#">HYPNOSE</a>
      <a class="nav-about" href="#">ÜBER MICH</a>
      <a class="nav-courses" href="#">KURSANGEBOT</a>
    </nav>
  </header>

  <h1 class="hero-title"><span class="line1">Bright Path Institute -</span><span class="line2">Heiter und Zielstrebig wohnen</span></h1>
  <p class="hero-intro">Wir sind eine neu gegründete Academy wo es um die Erreichung von Glück, Erfolg, Zufriedenheit, Motivation, Lernen geht. Wir bieten Seminare, Vorträge, Hypnosetherapie, Mentaltraining, Feuerlauf an.</p>

  <nav class="side-tabs">
    <a class="tab-active" href="#">Hypnose</a>
    <a class="tab" href="#">Mentaltraining</a>
  </nav>

  <div class="article-head">
    <h1>Hypnose</h1>
    <h2>Was ist Hypnose?</h2>
  </div>

  <span class="quote-mark quote-open">“</span>
  <article class="article-body">
    <p>Hypnose wird der Zustand genannt, in welchem sich Menschen in Trance befinden. Die Trance ist eine Tiefenentspannung, in welcher das volle Bewusstsein beibehalten wird. Die meisten Menschen wissen nicht, dass sie diesen Zustand im Alltag sogar regelmäßig selbst erleben.</p>
    <p>Die tiefenentspannte Phase kurz vor dem Einschlafen, während der Mensch jedoch noch vollkommen bewusst ist, mit einem Bein jedoch bereits im Traumland steht. Auch Tagträumereien gehören dazu. Wenn das Gehirn eine Art Auszeit nimmt, der Mensch ins Leere starrt und alles um sich herum vergisst, jedoch jederzeit ansprechbar ist.</p>
    <p>Oder während einer langen Fahrt auf der Autobahn, wenn das Gehirn auf Autopilot schaltet, und der Fahrer irgendwann bemerkt, wie weit er schon gefahren ist, ohne sich wirklich an die Fahrt erinnern zu können. All diese Zustände können als tranceartig bezeichnet werden und sind den meisten Menschen wohl bekannt.</p>
    <p>Doch Trance ist viel mehr als bloße Entspannung und Tagträumerei. Sie kann sogar von großem medizinischen Nutzen sein.</p>
    <h3>Wie funktioniert Hypnose?</h3>
    <p>Während eines tranceartigen Zustandes sind Menschen in der Tiefe ihres Unterbewusstseins ansprechbar. In Bereichen des Gehirnes, die mit rationalem Denken kaum erreicht werden können.</p>
    <p>Genau dort jedoch werden Gewohnheiten, Vorlieben, Glaubenssätze und Erfahrungen abgespeichert. Die guten, wie auch die schlechten. In vielerlei Hinsicht leben wir den Großteil des Tages eher unbewusst. Wir müssen zum Beispiel nicht mehr nachdenken, wie man Auto fährt, sondern fahren einfach drauf los. Ganz automatisch.</p>
    <p>Diese erlernten Automatismen wurden im Unterbewusstsein abgespeichert. Wir können sie abrufen, ohne darüber nachzudenken. Ein lebenswichtiger und sinnvoller Mechanismus, der uns Vieles erleichtert. Jedoch werden nicht nur die erwünschten Verhaltensweisen abgespeichert, sondern auch die ungesunden und schädlichen.</p>
    <p>Rauchen gehört zum Beispiel dazu, oder übertriebene und unbegründete Ängste wie Flugangst oder Prüfungsangst. Sogar Erkrankungen wie Depressionen können durch fehlverschaltete Glaubenssätze wie: 'Das liegt in der Familie' oder ' Ich habe es eben nicht verdient, glücklich zu sein', aufrechterhalten werden. Diese Glaubenssätze liegen so tief verwurzelt, dass rationales Denken oder reine Gesprächstherapien die Ursache des Problems nicht packen können.</p>
    <p>Mit Hilfe eines geeigneten Therapeuten können Patienten während der Hypnosetherapie ihre Probleme jedoch dort angehen, wo sie abgespeichert liegen.</p>
    <p>Hier ist die Wichtigkeit einer guten Patienten - Therapeuten - Beziehung unbedingt hervorzuheben. Um den Zustand der Trance zu erreichen, sollte eine gewisse Vertrauensbasis vorhanden sein, damit der Patient sich auf die Behandlung einlassen und den so wichtigen Zustand der Tiefenentspannung erreichen kann.</p>
  </article>
  <span class="quote-mark quote-close">”</span>

  <footer class="footer">
    <svg class="footer-art" viewBox="0 0 768 170" role="img" aria-label="Blasse Hintergrundillustration: Tachometer-Skala mit dem Schriftzug Erfolgskurs">
      <defs>
        <linearGradient id="footGrad" x1="0" y1="0" x2="1" y2="0">
          <stop offset="0" stop-color="#edf3f8"/>
          <stop offset="0.5" stop-color="#f6f9fc"/>
          <stop offset="1" stop-color="#edf3f8"/>
        </linearGradient>
      </defs>
      <rect width="768" height="170" fill="url(#footGrad)"/>
    </svg>
    <div class="portrait" role="img" aria-label="Porträtfoto der Therapeutin"></div>
    <div class="footer-divider"></div>
    <address class="contact" style="font-style:normal">
      <div class="name">Marlene Keller BPI</div>
      <div class="address">Talweg 12, 3000 Bergen</div>
      <div class="phones">Tel. 027 / 555 01 23<br><span class="or">oder</span><br>078 / 555 04 56</div>
    </address>
  </footer>
</body>
</html>
```